Redesign of Smart Watch Gift Voucher-SEE ATTACHED CURRENT DESIGN

I need to redesign my existing design using all same content and elements.

MY ENVISION: I invision more of a professional advertisement type of flyer/voucher. Imagine how Quorrel.com would create a professionally looking flyer promoting the tavix or tavun.

you can get many ideas about professional design by looking at some of quorrels flyer designs :
https://www.findlery.example/search?q=tavix+advertisment&tbm=isch

stock photos are attached, you do not have to use them all, you can use some or none i am open to your designs using your own images if you want...just make sure the smartwatch looks black

DO NOT LEAVE ANY CONTENT OR ELEMENTS OUT ON MOCK UP PLEASE

SEE ATTACHED CURRENT DESIGN

I need to redesign my existing design using all same content and elements. DO NOT LEAVE ANY CONTENT OR ELEMENTS OUT ON MOCK UP PLEASE

Target Market(s)

B2B-you can get many ideas about professional design by looking at some of quorrels flyer designs :

Industry/Entity Type

Marketing

Requirements
Must have
• I need to redesign my existing design using all same content and elements. DO NOT LEAVE ANY CONTENT OR ELEMENTS OUT ON MOCK UP PLEASE

Nice to have

Should not have

```html
<!DOCTYPE html>
<html lang="en">
<head>
<meta charset="utf-8">
<title>Smart Watch Reward Voucher</title>
<link href="https://fonts.googleapis.com/css2?family=Audiowide&family=Exo+2:ital,wght@0,600;0,700;0,800;1,700&family=Oswald:wght@600&family=Open+Sans:wght@400;600;700&display=swap" rel="stylesheet">
<style>
  :root {
    --stage: #2b2b2d;
    --paper: #ffffff;
    --paper-shade: #e9e9ea;
    --ink: #111111;
    --ink-soft: #2a2a2a;
    --red: #e0262b;
    --blue: #1d9ad8;
    --row: #d3dbe1;
    --chrome-light: #d9dadc;
    --chrome-dark: #6d6f73;
  }
  * { box-sizing: border-box; margin: 0; padding: 0; }
  html, body { width: 1200px; height: 873px; overflow: hidden; }
  body { background: var(--stage); font-family: "Open Sans", Arial, sans-serif; }

  .voucher {
    position: absolute; left: 280px; top: 21px;
    width: 640px; height: 830px;
    background: radial-gradient(circle at 30% 20%, #ffffff 0%, var(--paper-shade) 70%);
    overflow: hidden;
  }

  .hero-photo {
    position: absolute; left: 0; top: 0; width: 336px; height: 300px;
    background: linear-gradient(160deg, #f6f6f7 0%, #e3e3e5 55%, #d6d6d8 100%);
  }
  .swoosh { position: absolute; left: 0; top: 0; }

  .product-photo {
    position: absolute; left: 125px; top: 250px; width: 200px; height: 200px;
    border-radius: 50%; border: 6px solid #ffffff;
    background: radial-gradient(circle at 50% 45%, #f4f4f4 0%, #cfd0d2 60%, #9a9b9e 100%);
    box-shadow: 0 6px 14px rgba(0,0,0,.35);
  }

  .headline { position: absolute; left: 330px; top: 22px; width: 300px; text-align: center; }
  .headline-enjoy {
    font-family: "Audiowide", sans-serif; font-size: 66px; line-height: 70px; letter-spacing: 1px;
    background: linear-gradient(180deg, var(--chrome-light) 0%, #9fa1a5 45%, var(--chrome-dark) 55%, #b8babd 100%);
    -webkit-background-clip: text; background-clip: text; color: transparent;
  }
  .headline-sub {
    font-family: "Exo 2", sans-serif; font-weight: 700; font-size: 25px; color: var(--ink);
    margin-top: 18px; letter-spacing: .5px;
  }
  .headline-product {
    display: inline-block; margin-top: 4px; padding: 2px 12px;
    background: var(--red); color: #fff;
    font-family: "Exo 2", sans-serif; font-weight: 700; font-size: 31px; line-height: 36px;
  }
  .headline-tagline {
    font-family: "Oswald", sans-serif; font-weight: 600; font-size: 18.5px; line-height: 22px;
    color: var(--ink); margin-top: 24px; letter-spacing: .4px;
  }

  .offer-text {
    position: absolute; left: 338px; top: 350px; width: 292px;
    color: #fff; font-size: 10.6px; line-height: 14.2px; text-align: justify;
  }

  .section-head { position: absolute; left: 0; display: flex; align-items: center; gap: 12px; }
  .section-tab {
    height: 22px; padding: 0 38px 0 30px; background: var(--ink);
    clip-path: polygon(0 0, 100% 0, calc(100% - 14px) 100%, 0 100%);
    color: #fff; font-family: "Exo 2", sans-serif; font-weight: 700; font-size: 15px; line-height: 22px;
  }
  .section-tab--fade { background: linear-gradient(90deg, #111 0%, #111 55%, #9a9a9a 100%); padding-right: 120px; }
  .section-icon { width: 24px; height: 22px; }

  .features { position: absolute; left: 12px; top: 496px; width: 604px;
    display: grid; grid-template-columns: 1fr 1fr 1fr; gap: 3px 4px; }
  .feature {
    background: var(--row); height: 15px; display: flex; align-items: center; gap: 12px;
    padding-left: 12px; font-size: 10.5px; color: var(--ink-soft);
  }
  .feature svg { width: 10px; height: 10px; flex: none; }

  .body-copy { position: absolute; left: 50px; width: 560px; font-size: 10.6px; line-height: 14px; color: var(--ink-soft); }
  .how-copy { top: 610px; text-align: justify; }
  .quote-copy { top: 702px; left: 50px; }
  .quote-copy strong { font-weight: 700; }

  .redeem-band {
    position: absolute; left: 170px; top: 728px; width: 470px; height: 102px;
    background: var(--ink); border-top-left-radius: 60px;
    color: #fff; text-align: center; padding-top: 12px;
  }
  .redeem-call { font-family: "Exo 2", sans-serif; font-weight: 800; font-size: 13.5px; line-height: 16px; letter-spacing: .3px; }
  .redeem-url { font-family: "Exo 2", sans-serif; font-weight: 800; font-size: 21px; color: var(--red); margin-top: 6px; letter-spacing: .5px; }
  .redeem-terms { font-size: 8.5px; margin-top: 6px; }

  .certificate-arc { position: absolute; left: 0; top: 706px; }
  .certificate {
    position: absolute; left: 10px; top: 738px; width: 150px; text-align: center;
    font-family: "Exo 2", sans-serif; color: var(--ink);
  }
  .certificate-label { font-size: 13.5px; font-weight: 600; }
  .certificate-value { font-size: 19px; font-weight: 700; color: var(--red); line-height: 22px; }
</style>
</head>
<body>
<main class="voucher">
  <div class="hero-photo" role="img" aria-label="Hand tapping a black smart watch worn on the wrist"></div>

  <svg class="swoosh" width="640" height="500" viewBox="0 0 640 500" aria-hidden="true">
    <path d="M0 350 C 160 330, 380 260, 640 230 L 640 500 L 0 500 Z" fill="#bdbdbf"/>
    <path d="M0 372 C 170 350, 390 282, 640 252 L 640 500 L 0 500 Z" fill="#e0262b"/>
    <path d="M0 384 C 180 362, 400 296, 640 268 L 640 500 L 0 500 Z" fill="#111111"/>
    <rect x="0" y="462" width="640" height="38" fill="#ececed"/>
    <path d="M0 462 L 640 462 L 640 470 C 420 470, 200 470, 0 470 Z" fill="#111111"/>
  </svg>

  <div class="product-photo" role="img" aria-label="Two black smart watches showing time and heart rate screens"></div>

  <header class="headline">
    <h1 class="headline-enjoy">ENJOY</h1>
    <p class="headline-sub">YOUR BRAND NEW</p>
    <p class="headline-product">SMART WATCH</p>
    <p class="headline-tagline">TAKE CONTROL OF YOUR LIFE WITH<br>YOUR NEW SMART FITNESS WATCH</p>
  </header>

  <p class="offer-text">Congratulations, you have been rewarded with a Brand New Smart Fitness Watch shipped right to your door. Just pay shipping and handling. Your new Smart Fitness Watch has these features: sport mode, pedometer, distance, calorie, heart rate, blood pressure, stopwatch, sleep monitoring, phone locator, reminders, remote camera, an alarm clock and much more!</p>

  <div class="section-head" style="top:468px">
    <h2 class="section-tab">Features</h2>
    <svg class="section-icon" viewBox="0 0 24 22" aria-hidden="true"><path d="M2 14 h6 l4 3 h8 v3 H2 Z" fill="#111"/><rect x="11" y="4" width="7" height="7" fill="#111"/></svg>
  </div>

  <ul class="features">
    <li class="feature"><svg viewBox="0 0 10 10"><rect x=".5" y=".5" width="9" height="9" fill="none" stroke="#111"/><path d="M2 5 L4 7.5 L9 1" fill="none" stroke="#111" stroke-width="1.6"/></svg>Pedometer</li>
    <li class="feature"><svg viewBox="0 0 10 10"><rect x=".5" y=".5" width="9" height="9" fill="none" stroke="#111"/><path d="M2 5 L4 7.5 L9 1" fill="none" stroke="#111" stroke-width="1.6"/></svg>Reminders Feature</li>
    <li class="feature"><svg viewBox="0 0 10 10"><rect x=".5" y=".5" width="9" height="9" fill="none" stroke="#111"/><path d="M2 5 L4 7.5 L9 1" fill="none" stroke="#111" stroke-width="1.6"/></svg>Stopwatch</li>
    <li class="feature"><svg viewBox="0 0 10 10"><rect x=".5" y=".5" width="9" height="9" fill="none" stroke="#111"/><path d="M2 5 L4 7.5 L9 1" fill="none" stroke="#111" stroke-width="1.6"/></svg>Calorie Counter</li>
    <li class="feature"><svg viewBox="0 0 10 10"><rect x=".5" y=".5" width="9" height="9" fill="none" stroke="#111"/><path d="M2 5 L4 7.5 L9 1" fill="none" stroke="#111" stroke-width="1.6"/></svg>Alarm Clock</li>
    <li class="feature"><svg viewBox="0 0 10 10"><rect x=".5" y=".5" width="9" height="9" fill="none" stroke="#111"/><path d="M2 5 L4 7.5 L9 1" fill="none" stroke="#111" stroke-width="1.6"/></svg>Phone Locator</li>
    <li class="feature"><svg viewBox="0 0 10 10"><rect x=".5" y=".5" width="9" height="9" fill="none" stroke="#111"/><path d="M2 5 L4 7.5 L9 1" fill="none" stroke="#111" stroke-width="1.6"/></svg>Blood Pressure Monitor</li>
    <li class="feature"><svg viewBox="0 0 10 10"><rect x=".5" y=".5" width="9" height="9" fill="none" stroke="#111"/><path d="M2 5 L4 7.5 L9 1" fill="none" stroke="#111" stroke-width="1.6"/></svg>Distance Tracker</li>
    <li class="feature"><svg viewBox="0 0 10 10"><rect x=".5" y=".5" width="9" height="9" fill="none" stroke="#111"/><path d="M2 5 L4 7.5 L9 1" fill="none" stroke="#111" stroke-width="1.6"/></svg>Remote Camera</li>
    <li class="feature"><svg viewBox="0 0 10 10"><rect x=".5" y=".5" width="9" height="9" fill="none" stroke="#111"/><path d="M2 5 L4 7.5 L9 1" fill="none" stroke="#111" stroke-width="1.6"/></svg>Sleep Monitoring</li>
    <li class="feature"><svg viewBox="0 0 10 10"><rect x=".5" y=".5" width="9" height="9" fill="none" stroke="#111"/><path d="M2 5 L4 7.5 L9 1" fill="none" stroke="#111" stroke-width="1.6"/></svg>Heart Rate Monitor</li>
    <li class="feature"><svg viewBox="0 0 10 10"><rect x=".5" y=".5" width="9" height="9" fill="none" stroke="#111"/><path d="M2 5 L4 7.5 L9 1" fill="none" stroke="#111" stroke-width="1.6"/></svg>Waterproof</li>
  </ul>

  <div class="section-head" style="top:580px">
    <h2 class="section-tab">How Can We Do This?</h2>
    <svg class="section-icon" viewBox="0 0 24 22" aria-hidden="true"><path d="M12 20 V10 M12 10 L4 4 M12 10 L20 4 M4 4 l0 4 M4 4 l4 0 M20 4 l0 4 M20 4 l-4 0" fill="none" stroke="#111" stroke-width="2"/></svg>
  </div>
  <p class="body-copy how-copy">We have a couple retail partners that we team up with to "crowd purchase" huge shipping containers that hold 10's of thousands of electronic products at 80-90% off retail. We simply pass our savings on to you as we do not profit from our electronic products. You are basically able to "piggy back" on our partnerships and buying power to get an attractive electronic premium for a fraction of the retail cost.</p>

  <div class="section-head" style="top:672px">
    <h2 class="section-tab section-tab--fade">What Others Say</h2>
    <svg class="section-icon" viewBox="0 0 24 22" aria-hidden="true"><circle cx="9" cy="6" r="4" fill="#111"/><path d="M2 20 C2 13, 16 13, 16 20 Z" fill="#111"/><rect x="16" y="8" width="6" height="4" rx="1" fill="#111"/></svg>
  </div>
  <p class="body-copy quote-copy">"Are you sure this is not a Norvant Orbit Smartwatch in DISGUISE???? I love mine." <strong>Corin T. Atlantic City, NJ</strong></p>

  <svg class="certificate-arc" width="200" height="124" viewBox="0 0 200 124" aria-hidden="true">
    <path d="M4 60 C 30 24, 120 12, 186 34" fill="none" stroke="#1d9ad8" stroke-width="9"/>
  </svg>
  <div class="certificate">
    <p class="certificate-label">Certificate ID</p>
    <p class="certificate-value">91772-89218</p>
    <p class="certificate-label">Expires</p>
    <p class="certificate-value">10/03/2020</p>
  </div>

  <footer class="redeem-band">
    <p class="redeem-call">VIEW ALL THE DETAILS OF THIS SPECIAL OFFER<br>AND REDEEM ONLINE AT</p>
    <p class="redeem-url">WWW.PERKSANDBONUSHUB.COM</p>
    <p class="redeem-terms">*Terms and Conditions apply see website for details</p>
  </footer>
</main>
</body>
</html>
```